business card design for luxurious real estate brand

using the attached logo, i am looking for a 2-sided business card design. the back should be the gold logo on black background. the front needs to include: gold logo, name, phone, email, and website

Industry/Entity Type

real estate

Contact Information for Business Card

logo, name, email, phone, website

Font styles to use
Sans Serif

```html
<!DOCTYPE html>
<html lang="en">
<head>
<meta charset="utf-8">
<title>Casa Meridian – Business Card</title>
<link rel="stylesheet" href="https://fonts.googleapis.com/css2?family=Roboto:wght@400;500&family=Open+Sans:wght@400&display=swap">
<style>
  :root {
    --page: #ffffff;
    --card-base: #1c1c1f;
    --card-tone: #232327;
    --ink-black: #000000;
    --gold: #fdc90c;
    --white: #ffffff;
    --label: #111111;
  }
  * { margin: 0; padding: 0; box-sizing: border-box; }
  html, body { width: 1021px; height: 1200px; overflow: hidden; background: var(--page); }
  .sheet { position: relative; width: 1021px; height: 1200px; font-family: "Roboto", sans-serif; }

  .card {
    position: absolute; left: 139px; width: 754px; height: 431px; overflow: hidden;
  }
  .card--front { top: 91px; }
  .card--back { top: 596px; }

  .card__texture {
    position: absolute; inset: 0;
    background: radial-gradient(ellipse at 75% 30%, var(--card-tone), var(--card-base) 70%);
  }
  .card__shape { position: absolute; inset: 0; width: 100%; height: 100%; }

  .brand { position: absolute; display: flex; flex-direction: column; align-items: center; color: var(--gold); font-weight: 500; }
  .brand__mark { background: var(--gold); }
  .brand--small { left: 549px; top: 30px; width: 120px; }
  .brand--small .brand__mark { width: 34px; height: 34px; margin-bottom: 14px; }
  .brand--small .brand__name { font-size: 15px; letter-spacing: 3.5px; white-space: nowrap; }
  .brand--large { left: 0; right: 0; top: 106px; }
  .brand--large .brand__mark { width: 110px; height: 110px; margin-bottom: 48px; }
  .brand--large .brand__name { font-size: 38px; letter-spacing: 10px; white-space: nowrap; }

  .person { position: absolute; left: 97px; top: 172px; width: 280px; text-align: center; color: var(--white); }
  .person__name { font-size: 42px; font-weight: 500; line-height: 1; letter-spacing: 0.5px; }
  .person__role { font-size: 19px; font-weight: 400; margin-top: 4px; }

  .contact { position: absolute; display: flex; align-items: center; color: var(--white); font-size: 23px; white-space: nowrap; }
  .contact__icon {
    width: 35px; height: 35px; border-radius: 50%; background: var(--ink-black);
    border: 1px solid #3a3a3e; display: flex; align-items: center; justify-content: center; margin-right: 9px;
  }
  .contact__icon svg { width: 20px; height: 20px; }
  .contact--phone { left: 358px; top: 259px; }
  .contact--email { left: 332px; top: 303px; }
  .contact--web { left: 306px; top: 349px; }

  .size-label {
    position: absolute; left: 0; right: 0; top: 1050px; text-align: center;
    font-family: "Open Sans", sans-serif; font-size: 32px; color: var(--label);
  }
</style>
</head>
<body>
<div class="sheet">

  <section class="card card--front">
    <div class="card__texture" role="img" aria-label="Dark background with fine diagonal stripe pattern"></div>
    <svg class="card__shape" viewBox="0 0 1050 600" preserveAspectRatio="none" aria-hidden="true">
      <polygon fill="var(--ink-black)" points="0,0 210,0 332,213 455,0 702,0 360,600 305,600 84,218 0,358"/>
    </svg>

    <div class="brand brand--small">
      <span class="brand__mark"></span>
      <span class="brand__name">CASA MERIDIAN</span>
    </div>

    <div class="person">
      <h1 class="person__name">NAME HERE</h1>
      <p class="person__role">CEO &amp; CO-FOUNDER</p>
    </div>

    <div class="contact contact--phone">
      <span class="contact__icon">
        <svg viewBox="0 0 24 24"><path fill="var(--gold)" d="M6.6 10.8a15.1 15.1 0 0 0 6.6 6.6l2.2-2.2a1 1 0 0 1 1-.25 11.4 11.4 0 0 0 3.6.57 1 1 0 0 1 1 1V20a1 1 0 0 1-1 1A17 17 0 0 1 3 4a1 1 0 0 1 1-1h3.5a1 1 0 0 1 1 1c0 1.25.2 2.45.57 3.57a1 1 0 0 1-.25 1z"/></svg>
      </span>
      <span class="contact__text">0123 456 789</span>
    </div>
    <div class="contact contact--email">
      <span class="contact__icon">
        <svg viewBox="0 0 24 24"><circle cx="12" cy="12" r="3.8" fill="none" stroke="var(--gold)" stroke-width="2"/><path d="M15.8 12v1.6a2.4 2.4 0 0 0 4.8 0V12a8.6 8.6 0 1 0-3.4 6.9" fill="none" stroke="var(--gold)" stroke-width="2"/></svg>
      </span>
      <span class="contact__text">Your gmail adress goes here</span>
    </div>
    <div class="contact contact--web">
      <span class="contact__icon">
        <svg viewBox="0 0 24 24" fill="none" stroke="var(--gold)" stroke-width="1.5"><circle cx="12" cy="12" r="9"/><ellipse cx="12" cy="12" rx="4" ry="9"/><path d="M3 12h18M4.5 7.5h15M4.5 16.5h15"/></svg>
      </span>
      <span class="contact__text">Your website here</span>
    </div>
  </section>

  <section class="card card--back">
    <div class="card__texture" role="img" aria-label="Dark background with fine diagonal stripe pattern"></div>
    <div class="brand brand--large">
      <span class="brand__mark"></span>
      <span class="brand__name">CASA MERIDIAN</span>
    </div>
  </section>

  <p class="size-label">Size-3.5x2inch</p>
</div>
</body>
</html>
```